Business card for Property Management consultant

I need a business card for my business LX Vantage - I consult to real estate agents to improve the performance of their Property Management departments (rental houses management). The card needs to be very professional looking, incorporating our logo and my photo plus the line "Develop your Rent Roll to Perform"

Target Market(s)

Real Estate business owners

Industry/Entity Type

Business Consultant

Contact Information for Business Card

Business name - LX Vantage (logo uploaded)
My Name : Marcia Kellaway -
Title : Property Management Consultant

Develop your Rent Roll to perform

Phone : +61 438592716
email : marcia@lxvantage.com.au
website ; www.lxvantage.com.au

Requirements
Must have
• Logo
• My photo
• Very corporate / professional look

```html
<!DOCTYPE html>
<html lang="en">
<head>
<meta charset="utf-8">
<title>LX Vantage – Business Card</title>
<link href="https://fonts.googleapis.com/css2?family=Montserrat:wght@700;800&family=Roboto:wght@400;500;700&display=swap" rel="stylesheet">
<style>
  :root {
    --backdrop: #d9d9db;
    --card: #ffffff;
    --brand-blue: #1f58c4;
    --ink: #1b1b1b;
    --gold: #c8952a;
    --icon-blue: #2c5fc8;
    --photo-light: #f1d9cc;
    --photo-mid: #7a3b26;
    --photo-blue: #1f5ccf;
  }
  html, body {
    margin: 0;
    width: 1200px;
    height: 1200px;
    overflow: hidden;
    background: var(--backdrop);
  }
  .canvas {
    position: relative;
    width: 1200px;
    height: 1200px;
  }
  .card {
    position: absolute;
    left: 100px;
    top: 310px;
    width: 1000px;
    height: 580px;
    background: var(--card);
    border-radius: 48px;
    overflow: hidden;
    box-shadow: 0 14px 30px rgba(0,0,0,0.18);
  }
  .card__band {
    position: absolute;
    left: 0;
    right: 0;
    bottom: 0;
    height: 72px;
    background: var(--gold);
  }
  .card__slogan {
    position: absolute;
    z-index: 2;
    right: 70px;
    bottom: 24px;
    margin: 0;
    font-family: "Roboto", sans-serif;
    font-weight: 700;
    font-size: 22px;
    letter-spacing: 2px;
    color: #fff;
    white-space: nowrap;
  }
  .card__portrait {
    position: absolute;
    z-index: 1;
    left: 80px;
    top: 170px;
    width: 380px;
    height: 410px;
    border-radius: 190px 190px 0 0;
    background:
      radial-gradient(ellipse 45% 40% at 48% 32%, var(--photo-light) 0 55%, transparent 70%),
      radial-gradient(ellipse 60% 45% at 45% 22%, var(--photo-mid) 0 60%, transparent 75%),
      linear-gradient(180deg, #f4ebe6 0%, #e9d4c8 45%, var(--photo-blue) 72%, var(--photo-blue) 100%);
  }
  .brand {
    position: absolute;
    right: 70px;
    top: 56px;
    display: flex;
    align-items: center;
    gap: 16px;
  }
  .brand__mark {
    width: 34px;
    height: 34px;
    background: var(--gold);
  }
  .brand__name {
    font-family: "Montserrat", sans-serif;
    font-weight: 800;
    font-size: 54px;
    color: var(--ink);
    letter-spacing: 1px;
  }
  .identity {
    position: absolute;
    right: 70px;
    top: 180px;
    text-align: right;
  }
  .identity__name {
    margin: 0;
    font-family: "Montserrat", sans-serif;
    font-weight: 800;
    font-size: 46px;
    color: var(--brand-blue);
  }
  .identity__title {
    margin: 4px 0 0;
    font-family: "Roboto", sans-serif;
    font-size: 21px;
    letter-spacing: 1.5px;
    color: var(--ink);
  }
  .contacts {
    position: absolute;
    right: 70px;
    top: 318px;
    margin: 0;
    padding: 0;
    list-style: none;
    font-family: "Roboto", sans-serif;
    font-size: 20px;
    letter-spacing: 1.5px;
    color: var(--ink);
  }
  .contacts__item {
    display: flex;
    justify-content: flex-end;
    align-items: center;
    gap: 16px;
    height: 34px;
  }
  .contacts__icon {
    width: 20px;
    height: 20px;
    flex: none;
  }
</style>
</head>
<body>
<div class="canvas">
  <div class="card">
    <div class="card__band"></div>
    <p class="card__slogan">Develop your Rent Roll to perform</p>
    <div class="card__portrait" role="img" aria-label="Portrait photo of Marcia Kellaway in a blue jacket"></div>

    <div class="brand">
      <span class="brand__mark"></span>
      <span class="brand__name">LX Vantage</span>
    </div>

    <div class="identity">
      <p class="identity__name">Marcia Kellaway</p>
      <p class="identity__title">property management consultant</p>
    </div>

    <ul class="contacts">
      <li class="contacts__item">
        <span>+61 438592716</span>
        <svg class="contacts__icon" viewBox="0 0 20 20"><rect x="5" y="2" width="10" height="16" rx="2" fill="none" stroke="var(--icon-blue)" stroke-width="2"/></svg>
      </li>
      <li class="contacts__item">
        <span>marcia@lxvantage.com.au</span>
        <svg class="contacts__icon" viewBox="0 0 20 20"><rect x="2" y="4" width="16" height="12" fill="none" stroke="var(--icon-blue)" stroke-width="2"/><path d="M2 5l8 6 8-6" fill="none" stroke="var(--icon-blue)" stroke-width="2"/></svg>
      </li>
      <li class="contacts__item">
        <span>www.lxvantage.com.au</span>
        <svg class="contacts__icon" viewBox="0 0 20 20"><circle cx="10" cy="10" r="8" fill="var(--icon-blue)"/><path d="M2 10h16M10 2c3 3 3 13 0 16M10 2c-3 3-3 13 0 16" fill="none" stroke="#fff" stroke-width="1.4"/></svg>
      </li>
    </ul>
  </div>
</div>
</body>
</html>
```